Builders Worksite Corflute Outdoor Sign

We are a building company who are just branching out into new construction. How first new build is our own home which was designed by us and a local architect. We are proud and want to create more advertisement around our business.

We need a corflute sign that can staked outside the construction site and can be seen by people passing by.
Updates

Can we please make the company name and logo bigger (Tidewater Ridge Homes) This needs to be the focus. Can we please replace 'Manu' with 'Contact Us on 021-574-3619'

Target Market(s)

Home owners and people wishing to build on lifestyle blocks in New Zealand.

Font styles to use
Sans Serif

Requirements
Must have
• It needs to feature our:
Logo
Company name
Contact name and number - Manu - 0215743619
Landscape NOT portrait.

```html
<!DOCTYPE html>
<html lang="en">
<head>
<meta charset="utf-8">
<title>Tidewater Ridge Homes – Worksite Sign</title>
<link rel="stylesheet" href="https://fonts.googleapis.com/css2?family=Jost:wght@400&family=Montserrat:wght@900&display=swap">
<style>
  :root {
    --navy: #19223a;
    --yellow: #fdd20f;
    --phone-yellow: #fff200;
    --white: #ffffff;
    --backdrop: #d6d6d6;
  }
  * { margin: 0; padding: 0; box-sizing: border-box; }
  html, body {
    width: 1200px;
    height: 1000px;
    overflow: hidden;
    background: var(--backdrop);
  }
  .sign {
    position: absolute;
    left: 40px;
    top: 80px;
    width: 1120px;
    height: 840px;
    background: var(--navy);
    overflow: hidden;
  }
  .sign__band {
    position: absolute;
    left: 0;
    top: 140px;
    width: 100%;
    height: 374px;
    background: var(--yellow);
  }
  .brand {
    position: absolute;
    left: 280px;
    top: 47px;
    width: 560px;
    height: 560px;
    border-radius: 50%;
    background: var(--white);
    display: flex;
    flex-direction: column;
    align-items: center;
    justify-content: center;
    color: var(--navy);
    font-family: "Jost", sans-serif;
    font-weight: 400;
  }
  .brand__dot {
    width: 70px;
    height: 70px;
    border-radius: 50%;
    background: var(--yellow);
    margin-bottom: 34px;
  }
  .brand__name {
    font-size: 50px;
    line-height: 1;
    letter-spacing: 1px;
  }
  .brand__descriptor {
    margin-top: 26px;
    font-size: 36px;
    line-height: 1;
    letter-spacing: 22px;
    margin-right: -22px;
  }
  .contact {
    position: absolute;
    left: 0;
    top: 632px;
    width: 100%;
    text-align: center;
    font-family: "Montserrat", sans-serif;
    font-weight: 900;
  }
  .contact__label {
    display: flex;
    align-items: center;
    justify-content: center;
    gap: 20px;
    color: var(--white);
    font-size: 58px;
    line-height: 72px;
    margin-left: 20px;
  }
  .contact__icon {
    width: 72px;
    height: 72px;
    flex: none;
  }
  .contact__number {
    margin-top: 12px;
    color: var(--phone-yellow);
    font-size: 100px;
    line-height: 1;
    letter-spacing: 2px;
  }
</style>
</head>
<body>
  <main class="sign">
    <div class="sign__band"></div>

    <div class="brand">
      <div class="brand__dot"></div>
      <div class="brand__name">TIDEWATER RIDGE</div>
      <div class="brand__descriptor">HOMES</div>
    </div>

    <div class="contact">
      <p class="contact__label">
        <svg class="contact__icon" viewBox="0 0 72 72" aria-hidden="true">
          <circle cx="36" cy="36" r="36" fill="var(--white)"/>
          <path d="M24 17c2-1 4 0 5 2l4 8c1 2 0 4-1 5l-3 2c2 5 6 9 11 12l2-3c1-2 3-2 5-1l8 4c2 1 3 3 2 5l-2 5c-1 2-4 3-7 2-14-4-25-15-29-29-1-3 0-6 2-7z" fill="var(--navy)"/>
        </svg>
        CONTACT US ON
      </p>
      <p class="contact__number">021-574-3619</p>
    </div>
  </main>
</body>
</html>
```